New Company Introduction

We have launched a new business channel and need an online 'brochure' that we can use to announce us. Short, no more than 5 pages, clean, simple and changeable as we develop. See our new website for direction www.skyvellomedlift.example the introduction is to be issued to insurance companies, government departments and private clinics

Industry/Entity Type

Government

Font styles to use
Sans Serif

```html
<!DOCTYPE html>
<html lang="en">
<head>
<meta charset="UTF-8">
<title>About us – Medevac Consultancy Brochure</title>
<link rel="stylesheet" href="https://fonts.googleapis.com/css2?family=Open+Sans:wght@300&family=Carlito:wght@400&display=swap">
<style>
  :root {
    --backdrop: #e9e9e9;
    --page-white: #ffffff;
    --page-mist: #eef0f2;
    --accent-blue: #3e8acc;
    --divider-lavender: #9aaad8;
    --title-blue: #3f8fd2;
    --text-light: #ffffff;
    --photo-coat: #e8ecef;
    --photo-shade: #c9d3dc;
  }
  * { box-sizing: border-box; margin: 0; padding: 0; }
  html, body {
    width: 1200px;
    height: 971px;
    overflow: hidden;
    background: var(--backdrop);
  }
  .brochure-page {
    position: absolute;
    left: 46px;
    top: 134px;
    width: 1105px;
    height: 785px;
    display: flex;
    box-shadow: 0 2px 10px rgba(0,0,0,0.15);
  }
  .intro-panel {
    position: relative;
    width: 445px;
    height: 100%;
    background: linear-gradient(180deg, var(--page-mist) 0%, var(--page-white) 45%);
  }
  .section-title {
    position: absolute;
    left: 59px;
    top: 32px;
    font-family: "Open Sans", sans-serif;
    font-weight: 300;
    font-size: 50px;
    line-height: 64px;
    letter-spacing: -0.5px;
    color: var(--title-blue);
  }
  .doctor-photo {
    position: absolute;
    left: 8px;
    top: 254px;
    width: 300px;
    height: 531px;
    background: radial-gradient(ellipse at 45% 55%, var(--photo-shade) 0%, var(--photo-coat) 55%, rgba(255,255,255,0) 80%);
  }
  .panel-divider {
    width: 15px;
    height: 100%;
    background: var(--divider-lavender);
  }
  .content-panel {
    position: relative;
    width: 645px;
    height: 100%;
    background: var(--accent-blue);
    padding: 42px 55px 0 44px;
    font-family: "Carlito", "Calibri", sans-serif;
    font-size: 15.2px;
    line-height: 20.5px;
    color: var(--text-light);
  }
  .content-panel p {
    text-align: justify;
    margin-bottom: 15px;
  }
  .page-number {
    position: absolute;
    right: 13px;
    bottom: 8px;
    font-family: "Carlito", "Calibri", sans-serif;
    font-size: 14px;
    color: var(--text-light);
  }
</style>
</head>
<body>
  <main class="brochure-page">
    <section class="intro-panel">
      <h1 class="section-title">About us</h1>
      <div class="doctor-photo" role="img" aria-label="Photo of a senior doctor in a white coat with a stethoscope, holding a blue clipboard"></div>
    </section>
    <div class="panel-divider"></div>
    <section class="content-panel">
      <p>Our Medevac Service was originally part of our Private Charter service offered by our Sister company AeroNova Jets</p>
      <p>Like most private charter brokers we offered a service based around the basic disciplines of standard charter projects. Seeking availability, calculating positioning costs, appropriate airports and type tested crew were all the basic challenges of providing an excellent service in the private charter world. However, as our Medevac service grew, and we started to grow a reputation for being excellent in this field, it seemed only logical that we should separate the two disciplines. It was obvious to us that whilst all of the disciplines mentioned above were important, the extra layer of knowledge and experience required to properly support a service that could be as basic as organising a comfortable flight or as complicated as a multi-aircraft trans continental service, with multiple flight crews and medical teams, required us to invest in ourselves first.</p>
      <p>The training and professional development of our teams has helped us create one of the UKs leading Consultancy services for any movement of a individual, or group of people, that involves aircraft and medical support.</p>
      <p>As a Consultancy we do not own the aircraft, nor do we employ the flight crew or airbourne medical teams. This means we can maintain total focus on the Patient. We are not distracted by worrying about paying for an expensive fleet of aircraft, paying for staff when they are not being used and clearly have no conflicts of interest when it comes to selecting the most appropriate method of support. We have one concern, the Patient.</p>
      <p>We seek the best aircraft, flight crew, medical team and price for our Clients, quickly, efficiently and transparently. We have a global reach and utilise helicopters, small light aircraft, commercial carriers and private air ambulances. Whatever is right for the Patient is right for us.</p>
      <p>We provide our services to individuals, businesses, Northvale Health Trusts, insurance companies and private clinics.</p>
      <p>We are proud of what we do, and hope that you will be too.</p>
      <span class="page-number">Page 2</span>
    </section>
  </main>
</body>
</html>
```